Ferris Contracting LLC Business Card Design

I am looking for a creative and unique business card design. We are a commercial construction general contractor. With the name "FERRIS" Contracting, I am hoping to see some neat designs that correlate with the name.

```html
<!DOCTYPE html>
<html lang="en">
<head>
<meta charset="utf-8">
<title>Ferris Contracting LLC – Business Card</title>
<link rel="stylesheet" href="https://fonts.googleapis.com/css2?family=Montserrat:wght@400;500;800&display=swap">
<style>
  :root {
    --bg: #3a3b3d;
    --card: #1f2022;
    --card-edge: #2a93d5;
    --brand-blue: #2b9ee0;
    --text-light: #f1f2f3;
    --divider: #55585c;
  }
  * { box-sizing: border-box; margin: 0; padding: 0; }
  html, body {
    width: 1200px; height: 1200px; overflow: hidden;
    background: var(--bg);
    font-family: "Montserrat", sans-serif;
  }
  .canvas { position: relative; width: 1200px; height: 1200px; }
  .card {
    position: absolute; left: 240px;
    width: 720px; height: 412px;
    background: var(--card);
    border-radius: 30px;
    box-shadow: 0 0 0 2px var(--card-edge), 0 18px 40px rgba(0,0,0,.45);
    overflow: hidden;
  }
  .card--info { top: 150px; }
  .card--brand { top: 640px; }

  .wordmark {
    position: absolute;
    display: flex; align-items: center; gap: 14px;
    color: var(--brand-blue);
    font-weight: 800; letter-spacing: 2px; text-transform: uppercase;
    white-space: nowrap;
  }
  .wordmark__dot {
    width: 20px; height: 20px; border-radius: 50%;
    background: var(--brand-blue);
  }
  .card--info .wordmark { left: 185px; top: 90px; font-size: 30px; }
  .card--brand .wordmark { left: 50%; top: 50%; transform: translate(-50%, -50%); font-size: 44px; gap: 18px; }
  .card--brand .wordmark__dot { width: 28px; height: 28px; }

  .person { position: absolute; left: 70px; top: 278px; }
  .person__name {
    color: var(--brand-blue); font-weight: 800;
    font-size: 36px; letter-spacing: 2px; line-height: 1;
  }
  .person__title {
    color: var(--text-light); font-weight: 500;
    font-size: 18px; letter-spacing: 1px; margin-top: 6px;
  }

  .divider {
    position: absolute; left: 392px; top: 225px;
    width: 1px; height: 120px; background: var(--divider);
  }

  .contacts {
    position: absolute; left: 428px; top: 222px;
    list-style: none; display: flex; flex-direction: column; gap: 14px;
  }
  .contacts__item {
    display: flex; align-items: center; gap: 10px;
    color: var(--text-light); font-size: 18px; font-weight: 400;
  }
  .contacts__icon { width: 20px; height: 20px; flex: none; }
</style>
</head>
<body>
<main class="canvas">

  <section class="card card--info" aria-label="Business card, contact side">
    <div class="wordmark"><span class="wordmark__dot"></span>Ferris Contracting</div>

    <div class="person">
      <p class="person__name">FULL NAME</p>
      <p class="person__title">TITLE</p>
    </div>

    <div class="divider"></div>

    <ul class="contacts">
      <li class="contacts__item">
        <svg class="contacts__icon" viewBox="0 0 24 24" aria-hidden="true">
          <path fill="#2b9ee0" d="M6.6 10.8a15.1 15.1 0 0 0 6.6 6.6l2.2-2.2c.3-.3.7-.4 1-.2 1.1.4 2.3.6 3.6.6.6 0 1 .4 1 1V20c0 .6-.4 1-1 1A17 17 0 0 1 3 4c0-.6.4-1 1-1h3.5c.6 0 1 .4 1 1 0 1.3.2 2.5.6 3.6.1.3 0 .7-.2 1z"/>
        </svg>
        (000) 000 0000
      </li>
      <li class="contacts__item">
        <svg class="contacts__icon" viewBox="0 0 24 24" aria-hidden="true">
          <rect x="2" y="5" width="20" height="14" rx="1" fill="#2b9ee0"/>
          <path d="M2 6l10 7 10-7" fill="none" stroke="#1f2022" stroke-width="1.6"/>
        </svg>
        email@company.com
      </li>
      <li class="contacts__item">
        <svg class="contacts__icon" viewBox="0 0 24 24" aria-hidden="true">
          <g fill="none" stroke="#2b9ee0" stroke-width="1.8">
            <circle cx="12" cy="12" r="9.5"/>
            <ellipse cx="12" cy="12" rx="4.5" ry="9.5"/>
            <path d="M2.5 12h19M4 7h16M4 17h16"/>
          </g>
        </svg>
        www.company.com
      </li>
    </ul>
  </section>

  <section class="card card--brand" aria-label="Business card, brand side">
    <div class="wordmark"><span class="wordmark__dot"></span>Ferris Contracting</div>
  </section>

</main>
</body>
</html>
```